Modern Attractive Letterhead for Veterinary House Call Business.

A letterhead which can be printed on A4, A5 and A6 paper sizes.
To have: ( our files to be uploaded)
1. Logo with Text
2. telephone
3. email
4. website
5. Address

Target Market(s)

60-85year mainly women pet owners. Also market include families, young professionals, busy people who have dogs and cats

Industry/Entity Type

Business

Requirements
Must have
• 1. Logo with Text ( provided)
• 2. telephone
• 3. email
• 4. website
• 5. Address
Nice to have
• Needs to be modern, preferably warm and caring in nature( if possible )
Should not have
• difficulty in printing A5 and A6

```html
<!DOCTYPE html>
<html lang="en">
<head>
<meta charset="utf-8">
<title>Kind Care Vets – Letterhead</title>
<link rel="stylesheet" href="https://fonts.googleapis.com/css2?family=Arimo:wght@700&display=swap">
<style>
  :root {
    --paper: #ffffff;
    --leaf: #8dc63f;
    --ink-grey: #6d6e71;
    --brand-blue: #1f5fa8;
    --mist-blue: #e6eef7;
    --mist-green: #eef5e6;
  }
  html, body {
    margin: 0;
    padding: 0;
    overflow: hidden;
    background: var(--paper);
  }
  .letterhead {
    position: relative;
    width: 848px;
    height: 1200px;
    overflow: hidden;
    background: var(--paper);
    font-family: "Arimo", Arial, sans-serif;
  }
  .brand {
    position: absolute;
    left: 44px;
    top: 62px;
    display: flex;
    align-items: center;
    gap: 14px;
  }
  .brand-square {
    width: 34px;
    height: 34px;
    background: var(--brand-blue);
  }
  .brand-name {
    font-size: 34px;
    font-weight: 700;
    color: var(--brand-blue);
    letter-spacing: 0.5px;
    line-height: 1;
  }
  .tab-top {
    position: absolute;
    left: 725px;
    top: 0;
    width: 62px;
    height: 112px;
    background: var(--leaf);
  }
  .watermark {
    position: absolute;
    left: 0;
    top: 330px;
    width: 690px;
    height: 710px;
    background: radial-gradient(ellipse at 55% 45%, var(--mist-blue) 0%, rgba(238,245,230,0.6) 45%, rgba(255,255,255,0) 72%);
  }
  .band-bottom {
    position: absolute;
    left: 0;
    top: 1107px;
    width: 371px;
    height: 63px;
    background: var(--leaf);
  }
  .contact {
    position: absolute;
    top: 1106px;
    left: 380px;
    display: flex;
    color: var(--ink-grey);
    font-size: 17px;
    font-weight: 700;
    line-height: 22px;
  }
  .contact-address {
    width: 136px;
    text-align: right;
    padding-right: 14px;
  }
  .contact-divider {
    width: 1px;
    height: 62px;
    background: var(--ink-grey);
    margin-top: 2px;
  }
  .contact-reach {
    padding-left: 17px;
  }
  .contact p { margin: 0; }
</style>
</head>
<body>
  <main class="letterhead">
    <header class="brand">
      <span class="brand-square"></span>
      <span class="brand-name">Kind Care Vets</span>
    </header>
    <div class="tab-top"></div>

    <div class="watermark" role="img" aria-label="Large faint brand mark watermark"></div>

    <footer>
      <div class="band-bottom"></div>
      <div class="contact">
        <div class="contact-address">
          <p>PO Box 4520</p>
          <p>Maple Hollow</p>
          <p>QLD 4102</p>
        </div>
        <div class="contact-divider"></div>
        <div class="contact-reach">
          <p>0400123456</p>
          <p>www.kindcarevets.com.au</p>
          <p>info@kindcarevets.com.au</p>
        </div>
      </div>
    </footer>
  </main>
</body>
</html>
```